One slide graphic for website

I am designing a series of sliders for my website http://new.quillhartmedia.example

The slide I am trying to create has the following message:

EVERY company is a media company.
Empower yours now!

Learn More >

The ideas I have had for imagery are an office building with the letters 'Every Company is a Media Company' either shone onto the building or letters on the building roof ledge ect.

Aby ideas you may have to improve on this would be appreciated.

The idea behind the slide is to promote a software application which gives marketing professionals the chance to increase their media coverage. The message also encourages companies to create their own news on a number of platforms as the media landscape has changed so much. Look at the blue heron stunt whereby they generated 10 million views on clipvault using PR alone.

Good luck and I look forward to seeing your ideas.

Martin

```html
<!DOCTYPE html>
<html lang="en">
<head>
<meta charset="utf-8">
<title>Every company is a media company</title>
<link rel="stylesheet" href="https://fonts.googleapis.com/css2?family=Alegreya+Sans+SC:wght@800&family=Open+Sans:wght@300&display=swap">
<style>
  :root {
    --sky-light: #c9f1fb;
    --sky-mid: #4fc6e6;
    --sky-deep: #1a93c4;
    --ink: #000000;
    --paper: #ffffff;
    --stone: #8a8a8a;
    --panel-light: #f4f4f4;
    --panel-shade: #d9dde0;
  }
  html, body {
    margin: 0;
    padding: 0;
    overflow: hidden;
  }
  .slide {
    position: relative;
    width: 1200px;
    height: 387px;
    overflow: hidden;
    background: radial-gradient(ellipse 60% 75% at 42% 45%, var(--sky-light) 0%, var(--sky-mid) 50%, var(--sky-deep) 100%);
    font-family: "Alegreya Sans SC", "Arial Black", sans-serif;
  }
  .headline-box {
    position: absolute;
    left: 74px;
    top: 77px;
    width: 781px;
    height: 130px;
    background: var(--ink);
    color: var(--paper);
    display: flex;
    flex-direction: column;
    align-items: center;
    justify-content: center;
    text-align: center;
    line-height: 1;
  }
  .headline {
    margin: 0;
    font-weight: 800;
    font-size: 46px;
    letter-spacing: 1px;
    line-height: 54px;
    text-transform: none;
  }
  .headline .caps { font-size: 62px; text-transform: uppercase; }
  .tagline {
    position: absolute;
    left: 74px;
    width: 781px;
    top: 276px;
    margin: 0;
    text-align: center;
    color: var(--ink);
    font-weight: 800;
    font-size: 44px;
    word-spacing: 26px;
    letter-spacing: 1px;
  }
  .tagline .cap { font-size: 58px; }
  .showcase {
    position: absolute;
    left: 929px;
    top: 0;
    width: 271px;
    height: 387px;
    background: linear-gradient(160deg, var(--panel-light) 0%, var(--panel-shade) 55%, var(--panel-light) 100%);
    box-shadow: -6px 0 14px rgba(0, 0, 0, 0.25);
  }
  .browse-button {
    position: absolute;
    left: 948px;
    top: 106px;
    width: 209px;
    height: 132px;
    box-sizing: border-box;
    background: var(--paper);
    border: 3px solid var(--stone);
    color: #555555;
    font-family: "Open Sans", Arial, sans-serif;
    font-weight: 300;
    font-size: 38px;
    line-height: 48px;
    text-align: center;
    display: flex;
    flex-direction: column;
    justify-content: center;
    text-decoration: none;
  }
</style>
</head>
<body>
  <div class="slide">
    <div class="headline-box">
      <p class="headline"><span class="caps">Every</span> company is a<br>media company.</p>
    </div>
    <p class="tagline"><span class="cap">E</span>mpower yours now!</p>
    <div class="showcase" role="img" aria-label="Collage of tilted website page layouts"></div>
    <a class="browse-button" href="#">BROWSE<br>NOW!</a>
  </div>
</body>
</html>
```